bluegum ridge coaching needs snazzy business card that serves a dual purpose

business card needed for a Bluegum Ridge Coaching company that takes people out on the road to teach them proficiency on their bike.
My business logo is attached. I have grey and aqua colours with my logo.
i really like bitumen/tarmac/ road in the design somehow but that is up to you.
I think navy blue will go well with my colours too. see how you go.

I want this card to look REALLY good.
the back of the card may be used for emergency contact details too
In case of Emergency I am:
Name:

Emergency Contact name
emergency contact Phone number:

• details that are essential are:
• logo
• Name: Helena FORD
• ABN: 53 291 804 667
• phone number: 0455 128 906
• chatterly logo
• * ride tuition & proficiency
• * skills practice
• * maintenance 101
• * bike fitting service
• * cater for all ages & abilities
• backpage:
• logo
• skills confidence enjoyment
• some space for writing
• nothing girly. The business will already naturally attract women, it needs to appeal to both genders

```html
<!DOCTYPE html>
<html lang="en">
<head>
<meta charset="utf-8">
<title>Bluegum Ridge Coaching – Business Card</title>
<link rel="stylesheet" href="https://fonts.googleapis.com/css2?family=Exo+2:wght@400;500&display=swap">
<style>
  :root {
    --bg: #e6e4e1;
    --card-top: #f7f7f7;
    --card-bottom: #e4e5e6;
    --aqua: #5cc4b5;
    --charcoal: #3c3c3e;
    --text: #3a3a3a;
    --rule: #b9bcbf;
  }
  * { margin: 0; padding: 0; box-sizing: border-box; }
  html, body { width: 1200px; height: 903px; overflow: hidden; }
  body {
    background: var(--bg);
    font-family: "Exo 2", "Helvetica Neue", Arial, sans-serif;
    color: var(--text);
    position: relative;
  }
  .card {
    position: absolute;
    top: 294px;
    width: 540px;
    height: 315px;
    background: linear-gradient(160deg, var(--card-top), var(--card-bottom));
    box-shadow: 0 6px 18px rgba(0,0,0,.18);
    overflow: hidden;
  }
  .card--back { left: 40px; }
  .card--front { left: 620px; }

  .wordmark { color: var(--aqua); font-weight: 500; text-transform: uppercase; line-height: 1; }
  .wordmark__main { display: block; }
  .wordmark__sub { display: block; letter-spacing: .45em; }

  /* back */
  .card--back .wordmark { position: absolute; left: 0; right: 0; top: 34px; text-align: center; }
  .card--back .wordmark__main { font-size: 34px; letter-spacing: .04em; }
  .card--back .wordmark__sub { font-size: 13px; margin-top: 8px; padding-left: .45em; }
  .tagline {
    position: absolute; left: 0; right: 0; top: 104px; text-align: center;
    font-size: 12px; letter-spacing: .3em; text-transform: uppercase; color: var(--charcoal);
  }
  .tagline span { color: var(--aqua); padding: 0 .4em; }
  .emergency { position: absolute; left: 50px; right: 50px; top: 140px; }
  .emergency__title { font-size: 13px; font-weight: 500; color: var(--charcoal); margin-bottom: 6px; }
  .emergency__field {
    display: flex; align-items: flex-end; gap: 8px; height: 38px;
    font-size: 12px; color: var(--text);
  }
  .emergency__field::after { content: ""; flex: 1; border-bottom: 1px solid var(--rule); margin-bottom: 3px; }

  /* front */
  .band { position: absolute; background: var(--charcoal); }
  .band--top { left: 60px; top: 0; width: 90px; height: 26px; }
  .band--side { left: 300px; top: 128px; width: 240px; height: 26px; }

  .card--front .wordmark { position: absolute; left: 96px; top: 46px; }
  .card--front .wordmark__main { font-size: 30px; letter-spacing: .03em; }
  .card--front .wordmark__sub { font-size: 12px; margin-top: 8px; }

  .address { position: absolute; left: 40px; top: 152px; display: flex; gap: 8px; font-size: 12px; line-height: 1.45; }
  .address svg { flex: none; margin-top: 1px; }

  .services { position: absolute; left: 40px; top: 203px; list-style: none; font-size: 11px; }
  .services li { display: flex; align-items: center; gap: 8px; height: 17px; }
  .services li::before { content: ""; width: 5px; height: 5px; background: var(--aqua); flex: none; }

  .person { position: absolute; left: 300px; top: 164px; }
  .person__name { color: var(--aqua); font-size: 17px; font-weight: 500; letter-spacing: .08em; }
  .person__role { font-size: 13px; margin-top: 2px; }

  .contacts { position: absolute; left: 262px; top: 212px; list-style: none; font-size: 11px; }
  .contacts li { display: flex; align-items: center; gap: 8px; height: 17px; }
  .contacts svg { width: 11px; height: 11px; fill: var(--charcoal); flex: none; }
  .contacts .label { font-weight: 500; color: var(--charcoal); }
</style>
</head>
<body>
  <section class="card card--back" aria-label="Card back">
    <div class="wordmark">
      <span class="wordmark__main">Bluegum Ridge</span>
      <span class="wordmark__sub">Coaching</span>
    </div>
    <p class="tagline">Skills<span>•</span>Confidence<span>•</span>Enjoyment</p>
    <div class="emergency">
      <p class="emergency__title">In case of emergency I am:</p>
      <p class="emergency__field">Name:</p>
      <p class="emergency__field">Emergency contact name:</p>
      <p class="emergency__field">Emergency contact phone:</p>
    </div>
  </section>

  <section class="card card--front" aria-label="Card front">
    <div class="band band--top"></div>
    <div class="wordmark">
      <span class="wordmark__main">Bluegum Ridge</span>
      <span class="wordmark__sub">Coaching</span>
    </div>

    <div class="address">
      <svg width="12" height="16" viewBox="0 0 12 16"><path d="M6 0a6 6 0 0 0-6 6c0 4.5 6 10 6 10s6-5.5 6-10a6 6 0 0 0-6-6zm0 8.5A2.5 2.5 0 1 1 6 3.5a2.5 2.5 0 0 1 0 5z" fill="var(--aqua)"/></svg>
      <p>27 Ridgeline Parade<br>Wattle Flat</p>
    </div>

    <ul class="services">
      <li>Ride tuition &amp; proficiency</li>
      <li>Skills practice</li>
      <li>Maintenance 101</li>
      <li>Bike fitting service</li>
      <li>Cater for all ages &amp; abilities</li>
    </ul>

    <div class="band band--side"></div>
    <div class="person">
      <p class="person__name">HELENA FORD</p>
      <p class="person__role">Managing Director</p>
    </div>

    <ul class="contacts">
      <li><svg viewBox="0 0 12 12"><path d="M2.5 0 4.5 2.5 3.3 4a7 7 0 0 0 4.7 4.7L9.5 7.5 12 9.5 10.5 12C5 12 0 7 0 1.5z"/></svg>0455 128 906</li>
      <li><svg viewBox="0 0 12 12"><path d="M1 1h10v10H1zm2 2v6h6V3z"/></svg><span class="label">ABN</span>53 291 804 667</li>
      <li><svg viewBox="0 0 12 12"><path d="M0 2h12v8H0zm1 1 5 4 5-4z"/></svg>ride@bluegumridge.example</li>
      <li><svg viewBox="0 0 12 12"><path d="M6 0a6 6 0 1 0 0 12A6 6 0 0 0 6 0zm0 1c.9 0 1.8 2 2 4.5H4C4.2 3 5.1 1 6 1zM1 6.5h2c.1 2 .6 3.5 1.3 4.3A5 5 0 0 1 1 6.5zm3 0h4c-.2 2.5-1.1 4.5-2 4.5s-1.8-2-2-4.5zm5 0h2a5 5 0 0 1-3.3 4.3c.7-.8 1.2-2.3 1.3-4.3zM1 5.5a5 5 0 0 1 3.3-4.3C3.6 2 3.1 3.5 3 5.5zm8 0c-.1-2-.6-3.5-1.3-4.3A5 5 0 0 1 11 5.5z"/></svg>www.bluegumridge.example</li>
      <li><svg viewBox="0 0 12 12"><circle cx="6" cy="6" r="5.5"/></svg>chatterly / bluegumridge</li>
    </ul>
  </section>
</body>
</html>
```